Website design for Maple Nook Kidcare

I need a website designed for my daycare business, Maple Nook Kidcare, now that I have a new logo. My former website was ok but simple and I did not have a logo yet. It also was created by me using a template and was entirely pink. I loved the bright, happy feel of it but worried it might not appeal as much to potential clients who have sons. Therefore, I need a site which will appeal to both genders while still keeping the cheerful color scheme of my new logo, which has pinks, blue, green and cream.

Reason: Hello! I am still trying to download my new logo and am sorry it is taking me so long. Hopefully I will it posted by the end of today (US Eastern Standard Time). Thank you all very much for your patience!

Hello! I have finally managed to upload my new logo for you to use in designing my website. I'm sorry it took so long and greatly appreciate your time and creative efforts! I look forward to seeing what is submitted based on my logo design and its style/colors.

Many thanks!

Reason: As I've been traveling and posted my logo file late, I am extending my deadline. I am now back and can focus on providing more and better feedback. I appreciate your patience and submissions very much!

Reason: I need more time to provide feedback and make decisions.

Industry/Entity Type

Daycare

Colors
0192cd
33a6d7
86cae7
cadf82
fbf289
add136
e34197

```html
<!DOCTYPE html>
<html lang="en">
<head>
<meta charset="utf-8">
<title>Maple Nook Kidcare</title>
<link href="https://fonts.googleapis.com/css2?family=Carlito:wght@400;700&display=swap" rel="stylesheet">
<style>
  :root {
    --lime-bg: #cde082;
    --cream: #fde9b8;
    --nav-blue: #93d3dc;
    --nav-text: #6b4a2a;
    --body-text: #5a3a1a;
    --heading-grey: #6b5a4a;
    --leaf-green: #8cc63f;
    --pink: #e34197;
    --white: #ffffff;
  }
  * { margin: 0; padding: 0; box-sizing: border-box; }
  html, body { width: 1200px; height: 1137px; overflow: hidden; }
  body {
    background: var(--lime-bg);
    font-family: "Carlito", "Calibri", sans-serif;
    color: var(--body-text);
    position: relative;
  }
  .brand {
    position: absolute; left: 88px; top: 150px; width: 272px;
    font-size: 44px; line-height: 48px; font-weight: 700;
    color: var(--pink); text-align: center;
  }
  .hero {
    position: absolute; left: 437px; top: 72px; width: 705px; height: 255px;
    background: var(--cream); padding: 10px;
  }
  .hero-photo {
    width: 100%; height: 100%;
    background: linear-gradient(100deg, #f3dcc4 0%, #d9a582 35%, #b8825e 60%, #e9cbb0 100%);
  }
  .main-nav {
    position: absolute; left: 40px; top: 349px; width: 1102px; height: 31px;
    background: var(--nav-blue);
    display: flex; align-items: center; padding-left: 110px;
    font-size: 16px; font-weight: 700; color: var(--nav-text);
  }
  .main-nav a { color: inherit; text-decoration: none; }
  .main-nav .sep { margin: 0 18px; font-weight: 400; }
  .content {
    position: absolute; left: 40px; top: 380px; width: 1102px; height: 688px;
    background: var(--white);
  }
  .welcome { position: absolute; left: 32px; top: 78px; width: 200px; }
  .welcome h1 {
    font-size: 16px; line-height: 18px; font-weight: 400;
    color: var(--leaf-green); margin-bottom: 12px;
  }
  .welcome p { font-size: 12.5px; line-height: 17.7px; margin-bottom: 17px; }
  .art { position: absolute; }
  .art-tea-girl { left: 358px; top: 91px; width: 206px; height: 177px;
    background: linear-gradient(160deg, #e95a9c 0%, #93d3dc 55%, #a8d257 100%); border-radius: 10px; opacity: .85; }
  .art-stroller { left: 809px; top: 100px; width: 149px; height: 160px;
    background: linear-gradient(180deg, #f38bb0 0%, #93d3dc 60%, #7b4e34 100%); border-radius: 10px; opacity: .85; }
  .art-boy { left: 134px; top: 450px; width: 183px; height: 208px;
    background: linear-gradient(180deg, #7b4e34 0%, #f7c9a5 30%, #8cc63f 60%, #6b4a2a 100%); border-radius: 12px; opacity: .85; }
  .features {
    position: absolute; left: 352px; top: 277px; width: 719px; height: 353px;
    border: 7px solid var(--leaf-green); border-radius: 18px;
  }
  .feature { position: absolute; }
  .feature h2 {
    font-size: 19px; font-weight: 400; color: var(--heading-grey);
    letter-spacing: .3px; margin-bottom: 2px;
  }
  .feature p { font-size: 12.5px; line-height: 17.7px; }
  .feature .art { position: static; border-radius: 6px; margin-bottom: 6px; }
  .feature-learning { left: 41px; top: 34px; width: 170px; }
  .feature-learning .art { width: 88px; height: 123px; background: linear-gradient(180deg, #c9a07c, #4f6a60); }
  .feature-creativity { left: 258px; top: 18px; width: 180px; }
  .feature-creativity .art { width: 113px; height: 114px; background: linear-gradient(135deg, #b57b44, #e89a3a, #6fb0d8); border-radius: 50%; margin-bottom: 14px; }
  .feature-sharing { left: 479px; top: 22px; width: 185px; }
  .feature-sharing .art { width: 79px; height: 110px; background: linear-gradient(180deg, #cfe3ea, #f1c7cf); margin-bottom: 15px; }
</style>
</head>
<body>
  <div class="brand">Maple Nook Kidcare</div>

  <div class="hero">
    <div class="hero-photo" role="img" aria-label="Photo of three smiling children with their heads close together"></div>
  </div>

  <nav class="main-nav">
    <a href="#">Home</a><span class="sep">|</span>
    <a href="#">About Us</a><span class="sep">|</span>
    <a href="#">Services</a><span class="sep">|</span>
    <a href="#">Hours &amp; Fees</a><span class="sep">|</span>
    <a href="#">Policies</a><span class="sep">|</span>
    <a href="#">Contact Us</a><span class="sep">|</span>
    <a href="#">Photos</a><span class="sep">|</span>
    <a href="#">Testimonials</a>
  </nav>

  <main class="content">
    <section class="welcome">
      <h1>Welcome to Maple Nook Kidcare, a playspace where children can play, create, and imagine!</h1>
      <p>Welcome to Maple Nook Kidcare, a licensed Group Family Day Care, located in Riverton's beautiful Hillcrest district. We are located on a pretty, tree-lined block on Linden Lane, between Oak and Birch Avenues. We are a few blocks from the Green Line tram and the Elm Street bus route, and we offer flexible hourly childcare, making it as easy as possible for busy parents on the go to arrange their children's care.</p>
      <p>We invite you to learn more about us and hope you will visit us soon!</p>
    </section>

    <div class="art art-tea-girl" role="img" aria-label="Illustration of a girl at a tea table with a green teapot"></div>
    <div class="art art-stroller" role="img" aria-label="Illustration of a baby in a blue and pink stroller with a bird"></div>
    <div class="art art-boy" role="img" aria-label="Illustration of a sitting boy in a green shirt waving"></div>

    <section class="features">
      <article class="feature feature-learning">
        <div class="art" role="img" aria-label="Photo of a child learning"></div>
        <h2>LEARNING</h2>
        <p>We develop age-appropriate activities that introduce and strengthen academic and social skills.</p>
      </article>
      <article class="feature feature-creativity">
        <div class="art" role="img" aria-label="Illustration of a paint palette with brushes"></div>
        <h2>CREATIVITY</h2>
        <p>We offer children a wide range of creative opportunities including art projects, toddler yoga lessons, afternoon tea parties, dress up play, and a large selection of books and games.</p>
      </article>
      <article class="feature feature-sharing">
        <div class="art" role="img" aria-label="Illustration of a floral teapot and teacup"></div>
        <h2>SHARING</h2>
        <p>We strive to include enrichment activities that extend your child's understanding of the world and their role in it. During our tea parties, for instance, we teach and emphasize good manners so that your child can learn their benefits as they grow.</p>
      </article>
    </section>
  </main>
</body>
</html>
```